Hollow Lantern Town Strolling Past Tour

We are launching a different kind of city historical walking tour company with a slightly darker approach using historical but real stories that have long been forgotten from living memory.
Our tour is going to contain a lot of very thoroughly researched stories ranging from 50 to 150 years past that takes the customer into the actual-real life past of the city streets.  Stories that may contains some dark undertones and stories with a twist or that seem eccentric to us now but were entirely normal back in olden times - minus the dry historical facts that most tours engage in..
Our tours are going to run both day and night and will incorporate real history / real Hollow Lantern, so some of the stories will be quite serious (e.g.- there are actual murders from 100 years ago, baffling court cases, even a bit of poetry written by murderers, suicides, love triangles, you name it.  We are aiming for a mystery/history theme and are aiming to attract tourists who are interested in getting a different kind of history.

We're not going for scares and even though we expect people to enjoy our tours;  we're not aiming at light fun and frivolity.  I guess if you wanted to give us a tv rating we'd be aiming at M to MA15+.
If I was to give you another analogy using the literature world.  Think Edwin Harrowgates Nightwarden rather than the Moonveil Saga of movies.  Or Agnes Pellowe's Corvanthus rather than the Grimbles.  Even Crown of Embers rather than a soap opera.
Our stories are being carefully crafted and are packed with unexpected twists, turns & revelations whilst remaining all 100% true.  We have approx 15-20 stories for each tour and we're designing them in a way that each story will trigger a different range of emotions in the listeners on a regular basis.  We're being very careful to keep it fresh for each story so that it will next to impossible for our guests to zone out!  I personally can't stand going on a tour where mildly interesting facts are read out.  We like deep, rich stories rather than pop entertainment.
We want the website to generate a feeling/atmosphere for our product that draws the right crowd to our tours as well as making it easy to make a booking.  Basic features to include:-
Home Page
Bookings Page
Integration with a booking system will be required here via use of plugin code.
Private Functions Page
We are hoping to integrate with a booking system via use of plugin code.  If not, then a simple form enquiry type input e.g.- name, emails, subject, contact, details, preferred date/time, etc).
About Us Page :-
Dark; a euphemism for the unknown or the forgotten.  Think dark ages, dark matter, dark energy; things where knowledge is uncertain or unknown are often termed dark.   Hollow Lantern brings back the hidden past, the forgotten past, the past that may not want to be remembered……but these are real stories....real stories that come from the streets around you.

Some of these stories may be tales of dark things.....some may simply be a charming reminder of days gone by…..regardless these stories are compelling reminders of the amazing times that precede us…..and the forgotten people of yesteryear finally get a chance to have their story told to a fresh audience.  Through you, the people of yesterday get to live again.  Will you like what you hear?

Contact Us page:-
•	A form input type page.
•	Include space for our phone number
•	Include space for our email address
Other Items:-
Social Media Links; we will be looking for social media icons to link to our social media pages to Friendloop, Snapvista, Chirpline.
Subscription; we want to also capture an input email address box for site visitors.  We will be launching a weekly Hollow Lantern podcast / email newsetter; with a weekly Hollow Lantern from a different place in the world and we want some way for people to subscribe.

Updates
Project Deadline Extended
Reason: A few additional photos have been uploaded.  Feel free to utilize if helpful.  Our stories range from the 1800s to 1950s in an era with beautiful old Victorian buildings.  I'm putting through the extension just to give some more time to see if this gives any more ideas and inspiration.  Thank you for all the great submissions.

Target Market(s)
Tourists that want to hear a darker version of the city they are visiting. Stories that other tour companies would not even think of covering. The real history of the events that ordinary people lived through that didn't necessarily make the history books. All stories are true; as per project description.
Industry/Entity Type
Tourism
Coding
Coded - Design and coding required
Number of Pages Required
5+ page
Colors
Designer to choose colors to be used in the design.
Look and feel

```html
<!DOCTYPE html>
<html lang="en">
<head>
<meta charset="utf-8">
<title>Hollow Lantern Town Strolling Past Tour</title>
<link rel="stylesheet" href="https://fonts.googleapis.com/css2?family=Poppins:ital,wght@0,300;0,400;0,500;0,600;0,700;1,400&display=swap">
<style>
:root{
  --black:#0c0c0c;
  --nav:#2a2a2a;
  --band:#1d1d1d;
  --brown:#4b3317;
  --stories:#222222;
  --footer:#1f1f1f;
  --bottom:#171717;
  --red:#e3262e;
  --white:#ffffff;
  --muted:#9a9a9a;
  --field:#3a3a3a;
}
*{margin:0;padding:0;box-sizing:border-box}
html,body{width:1200px;height:2586px;overflow:hidden}
body{font-family:'Poppins',sans-serif;background:var(--black);color:var(--white);position:relative}
.abs{position:absolute}

/* top bar */
.topbar{left:0;top:0;width:1200px;height:55px;background:var(--black);font-size:13px}
.topbar .contact{left:130px;top:18px;display:flex;gap:34px;align-items:center}
.topbar .contact span{display:flex;align-items:center;gap:10px}
.topbar .right{right:130px;top:13px;height:28px;display:flex;align-items:center;gap:30px}
.topbar .social{display:flex;gap:16px;font-size:11px;color:#ddd;white-space:nowrap}
.topbar .user{display:flex;align-items:center;gap:10px;font-size:13px;white-space:nowrap}
.avatar{width:28px;height:28px;border-radius:50%;background:#cfcfcf;flex:none}

/* nav */
.nav{left:0;top:55px;width:1200px;height:69px;background:var(--nav)}
.brand{left:130px;top:23px;display:flex;align-items:center;gap:8px;font-weight:700;font-size:16px;letter-spacing:.5px}
.brand .mark{width:22px;height:22px;background:var(--red)}
.menu{left:410px;top:25px;display:flex;gap:39px;font-size:13px;color:#e6e6e6;align-items:center;white-space:nowrap}
.menu .active{position:relative}
.menu .active::after{content:"";position:absolute;left:-2px;right:-2px;top:42px;height:3px;background:var(--red)}

/* hero */
.hero{left:0;top:124px;width:1200px;height:466px;background:linear-gradient(180deg,#6f9ed8 0%,#a9c4e4 40%,#8d8f88 62%,#56667a 78%,#3f5a3a 100%)}
.hero h1{left:167px;top:196px;font-size:34px;font-weight:500;text-shadow:0 2px 6px rgba(0,0,0,.4);white-space:nowrap}
.hero h2{left:167px;top:262px;font-size:34px;font-weight:700;letter-spacing:1px}
.hero p{left:167px;top:336px;font-size:15px;white-space:nowrap}
.btn{background:var(--red);color:var(--white);font-weight:600;font-size:11px;text-transform:uppercase;display:flex;align-items:center;justify-content:center;white-space:nowrap}
.hero .btn{left:167px;top:385px;width:195px;height:43px}
.dots{left:588px;top:433px;display:flex;gap:8px}
.dots i{width:13px;height:13px;border-radius:50%;border:2px solid #ddd;display:block}
.dots i.on{background:#fff;box-shadow:inset 0 0 0 3px #333}

/* quote */
.quote{left:0;top:590px;width:1200px;height:138px;background:var(--band)}
.quote .mark{left:130px;top:50px;font-size:46px;font-weight:700;font-style:italic;line-height:1}
.quote p{left:184px;top:52px;width:900px;font-size:16px;font-style:italic;line-height:26px;color:#e8e8e8}

/* about */
.about{left:0;top:728px;width:1200px;height:474px;background:linear-gradient(180deg,#2f2f2f,#262626)}
.about h3{left:129px;top:70px;font-size:17px;font-weight:700;text-transform:uppercase}
.about .text{left:129px;top:115px;width:600px;font-size:12px;line-height:22px;color:var(--muted)}
.about .text p+p{margin-top:12px}
.about .learn{left:129px;top:336px;width:131px;height:43px;border-radius:22px}
.search{left:779px;top:77px;width:292px}
.search label{font-size:12px;color:#5e5e5e;display:block;height:20px}
.field{height:38px;background:var(--field);display:flex;align-items:center;justify-content:space-between;padding:0 14px;font-size:11px;color:#aaa}
.search .btn{height:40px;margin-top:26px;width:100%;border-radius:0}

/* packages */
.packages{left:0;top:1202px;width:1200px;height:496px;background:linear-gradient(180deg,#4e351a,#3e2c18)}
.packages h3{left:129px;top:76px;font-size:26px;font-weight:400}
.card{width:210px;top:151px}
.card .img{width:210px;height:150px}
.card h4{font-size:13px;font-weight:600;margin-top:26px}
.stars{margin-top:8px;display:flex;align-items:center;gap:6px;font-size:11px;color:var(--red)}
.stars span{font-size:10px;color:#aaa}

/* stories */
.stories{left:0;top:1698px;width:1200px;height:376px;background:var(--stories)}
.stories h3{left:129px;top:60px;font-size:21px;font-weight:400;display:flex;align-items:center;gap:16px}
.stories .all{left:955px;top:66px;font-size:14px;font-style:italic;color:var(--red)}
.stories .img{top:122px;width:210px;height:197px}

/* footer */
.footer{left:0;top:2074px;width:1200px;height:426px;background:var(--footer)}
.vline{top:40px;width:1px;height:345px;background:#333}
.f-logo{left:145px;top:59px;width:62px;height:62px;border-radius:50%;background:var(--red)}
.footer h3{left:138px;top:138px;font-size:30px;font-weight:700}
.footer .about-text{left:138px;top:203px;width:276px;font-size:12.5px;line-height:22px;color:#bdbdbd}
.footer h5{font-size:12px;font-weight:700;letter-spacing:1px;text-transform:uppercase}
.recent{left:464px;top:64px;width:274px}
.recent .item{display:flex;gap:16px;padding:24px 0 38px;border-bottom:1px solid #2f2f2f;font-size:12.5px;height:93px}
.recent .item:first-of-type{padding-top:20px}
.recent .item:last-child{border:none}
.recent .thumb{width:55px;height:55px;flex:none}
.info{left:788px;top:64px;font-size:12.5px;color:#bdbdbd}
.info p{margin-top:26px}
.info p+p{margin-top:20px}
.info .social{display:flex;gap:16px;margin-top:34px;font-size:11px;color:#fff}

.copy{left:0;top:2500px;width:1200px;height:86px;background:var(--bottom);display:flex;align-items:center;justify-content:center;font-size:12px;color:#6a6a6a}
</style>
</head>
<body>

<header class="abs topbar">
  <div class="abs contact">
    <span><svg width="13" height="13" viewBox="0 0 24 24"><path fill="#fff" d="M6.6 10.8a15 15 0 0 0 6.6 6.6l2.2-2.2a1 1 0 0 1 1-.25 11 11 0 0 0 3.6.6 1 1 0 0 1 1 1V20a1 1 0 0 1-1 1A17 17 0 0 1 3 4a1 1 0 0 1 1-1h3.5a1 1 0 0 1 1 1 11 11 0 0 0 .6 3.6 1 1 0 0 1-.25 1z"/></svg>1.98.765432</span>
    <span><svg width="14" height="12" viewBox="0 0 24 20"><rect x="1.5" y="1.5" width="21" height="17" fill="none" stroke="#fff" stroke-width="2"/><path d="M2 2l10 9 10-9" fill="none" stroke="#fff" stroke-width="2"/></svg>info@hollowlantern.example</span>
  </div>
  <div class="abs right">
    <nav class="social" aria-label="Social links">
      <span>Friendloop</span><span>Dotframe</span><span>Circlespace</span><span>Chirpline</span>
    </nav>
    <div class="user"><span class="avatar"></span>admin <svg width="8" height="5" viewBox="0 0 8 5"><path d="M0 0h8L4 5z" fill="#fff"/></svg></div>
  </div>
</header>

<div class="abs nav">
  <div class="abs brand"><span class="mark"></span>Hollow Lantern</div>
  <nav class="abs menu">
    <span class="active">Home</span><span>About Us</span><span>Book Now</span><span>Private Fucntions</span><span>All Tours</span><span>Faq</span><span>Contact Us</span>
    <svg width="13" height="13" viewBox="0 0 24 24"><circle cx="10" cy="10" r="7" fill="none" stroke="#fff" stroke-width="3"/><path d="M15 15l7 7" stroke="#fff" stroke-width="3"/></svg>
  </nav>
</div>

<section class="abs hero" role="img" aria-label="City skyline with a steel truss bridge over a river">
  <h1 class="abs">City historical walking tour company</h1>
  <h2 class="abs">BRISBANE</h2>
  <p class="abs">orem ipsum orem ipsum orem ipsum orem ipsum</p>
  <div class="abs btn">Read More Hollow Lantern</div>
  <div class="abs dots"><i></i><i class="on"></i></div>
</section>

<section class="abs quote">
  <span class="abs mark">“</span>
  <p class="abs">There were bits of spines, bits of skulls, &amp; finger bones spilled out all over the streets – I ended up filling three boxes. Children were playing with them for weeks</p>
</section>

<section class="abs about" role="img" aria-label="Faded sepia photograph of an old city street">
  <h3 class="abs">About City Historical Walking Tour Company</h3>
  <div class="abs text">
    <p>Dark; a euphemism for the unknown or the forgotten. Think dark ages, dark matter, dark energy; things where knowledge is uncertain or unknown are often termed dark. Hollow Lantern brings back the hidden past, the forgotten past, the past that may not want to be remembered……but these are real stories....real stories that come from the streets around you.</p>
    <p>Some of these stories may be tales of dark things.....some may simply be a charming reminder of days gone by…..regardless these stories are compelling reminders of the amazing times that precede us…..and the forgotten people of yesteryear finally get a chance to have their story told to a fresh audience. Through you, the people of yesterday get to live again. Will you like what you hear?</p>
  </div>
  <div class="abs btn learn">Learn More</div>
  <form class="abs search">
    <label>Keywords</label>
    <div class="field"><span></span><svg width="11" height="11" viewBox="0 0 24 24"><circle cx="10" cy="10" r="7" fill="none" stroke="#fff" stroke-width="3"/><path d="M15 15l7 7" stroke="#fff" stroke-width="3"/></svg></div>
    <label style="margin-top:32px"></label>
    <div class="field"><span>Any</span><svg width="8" height="5" viewBox="0 0 8 5"><path d="M0 0h8L4 5z" fill="#ccc"/></svg></div>
    <label style="margin-top:30px"></label>
    <div class="field" style="color:#777"><span>Any</span><svg width="11" height="11" viewBox="0 0 12 12"><rect x="1" y="2" width="10" height="9" fill="none" stroke="#bbb"/><path d="M1 5h10" stroke="#bbb"/></svg></div>
    <div class="btn">Search</div>
  </form>
</section>

<section class="abs packages">
  <h3 class="abs">Popular Tour Packages</h3>
  <article class="abs card" style="left:129px"><div class="img" role="img" aria-label="Rooftops of heritage city buildings" style="background:linear-gradient(180deg,#4a6ea8,#8c7d70)"></div><h4>Tour4</h4><div class="stars">☆☆☆☆☆ <span>(0 Review)</span></div></article>
  <article class="abs card" style="left:372px"><div class="img" role="img" aria-label="River bridge and city skyline" style="background:linear-gradient(180deg,#4f86d0,#8aa5b6 60%,#5a7384)"></div><h4>Tour3</h4><div class="stars">☆☆☆☆☆ <span>(0 Review)</span></div></article>
  <article class="abs card" style="left:617px"><div class="img" role="img" aria-label="Sandstone clock tower with palm trees" style="background:linear-gradient(180deg,#2f6ec6,#a88a5c 55%,#3f6b3a)"></div><h4>Tour2</h4><div class="stars">☆☆☆☆☆ <span>(0 Review)</span></div></article>
  <article class="abs card" style="left:860px"><div class="img" role="img" aria-label="Red brick Victorian cathedral" style="background:linear-gradient(180deg,#3f78cf,#9a4f38 55%,#6d5a3c)"></div><h4>Tour1</h4><div class="stars">☆☆☆☆☆ <span>(0 Review)</span></div></article>
</section>

<section class="abs stories">
  <h3 class="abs"><svg width="14" height="18" viewBox="0 0 14 18"><circle cx="7" cy="6" r="5" fill="none" stroke="#e3262e" stroke-width="2"/><path d="M5 14h4M5 17h4" stroke="#e3262e" stroke-width="2"/></svg>Hollow Lantern</h3>
  <span class="abs all">/ &nbsp;Read All Articles</span>
  <div class="abs img" style="left:129px;background:linear-gradient(180deg,#d8d8d8,#555)" role="img" aria-label="Black and white photo of an old street with a tram"></div>
  <div class="abs img" style="left:372px;background:linear-gradient(180deg,#cfcfcf,#4c4c4c)" role="img" aria-label="Black and white photo of a crowded street with carriages"></div>
  <div class="abs img" style="left:617px;background:linear-gradient(180deg,#bfb3a0,#5c5447)" role="img" aria-label="Sepia photo of a busy historic street with trams"></div>
  <div class="abs img" style="left:860px;background:linear-gradient(180deg,#a8a08f,#6f685b)" role="img" aria-label="Sepia photo of old excavated remains"></div>
</section>

<footer class="abs footer">
  <div class="abs vline" style="left:436px"></div>
  <div class="abs vline" style="left:762px"></div>
  <div class="abs f-logo"></div>
  <h3 class="abs">About Us</h3>
  <p class="abs about-text">Dark; a euphemism for the unknown or the forgotten. Think dark ages, dark matter, dark energy; things where knowledge is uncertain or unknown are often termed dark. Hollow Lantern brings back the hidden past, the forgotten past, the past that may not want to be remembered.....but these are real stories....real stories that come from the streets around you.</p>
  <div class="abs recent">
    <h5>Recent Tours</h5>
    <div class="item"><div class="thumb" role="img" aria-label="Heritage rooftops" style="background:linear-gradient(#4a6ea8,#8c7d70)"></div>Tour4</div>
    <div class="item"><div class="thumb" role="img" aria-label="River bridge" style="background:linear-gradient(#4f86d0,#5a7384)"></div>Tour3</div>
    <div class="item"><div class="thumb" role="img" aria-label="Clock tower" style="background:linear-gradient(#2f6ec6,#a88a5c)"></div>Tour2</div>
  </div>
  <div class="abs info">
    <h5 style="color:#fff">Contact Info</h5>
    <p>Address : 48 Gaslight Lane, Old Quarter</p>
    <p>Phone : +61 7 5550 1842</p>
    <p style="margin-top:8px">hello@hollowlantern.example</p>
    <div class="social"><span>Friendloop</span><span>Chirpline</span><span>Linkwise</span><span>Pinboardly</span><span>Reelnest</span></div>
  </div>
</footer>

<div class="abs copy">Copyright 2017 Hollow Lantern Walks, All Right Reserved</div>

</body>
</html>
```